Personal Injury Billboard for a law frim

Our firm has a billboard we need art for. It will specifically for personal injury cases. The dimensions of art the billboard are 9 ft high 29 feet wide.

We want to highlight the terms, "Serious Injuries" and "Trusted. Local. Experienced." We want to incorporate the attached "Brightvale Honors" badge as well as our attached firm logo. We want the blue color scheme (see attached).

Maybe an image of an industrial plant in the background?

Sans Serif

```html
<!DOCTYPE html>
<html lang="en">
<head>
<meta charset="utf-8">
<title>Halvern Ostrand Pike — Serious Injuries Billboard</title>
<link href="https://fonts.googleapis.com/css2?family=Bebas+Neue&family=Montserrat:wght@500;600&family=Poppins:wght@600;700;800&display=swap" rel="stylesheet">
<style>
  :root{
    --page:#dbeaf6;
    --navy:#0b2566;
    --navy-deep:#061a4d;
    --royal:#1b4f9c;
    --sky:#3a95d4;
    --white:#ffffff;
    --ink:#111111;
    --link:#1f6fb8;
  }
  *{margin:0;padding:0;box-sizing:border-box}
  html,body{width:1200px;height:670px;overflow:hidden;background:var(--page)}
  .billboard{position:absolute;left:49px;top:164px;width:1102px;height:341px;overflow:hidden;background:var(--navy)}
  .backdrop{position:absolute;inset:0;background:
      radial-gradient(ellipse at 55% 30%, rgba(70,120,190,.55), transparent 60%),
      linear-gradient(180deg,var(--royal) 0%,var(--navy) 60%,var(--navy-deep) 100%)}
  .brand-panel{position:absolute;left:0;top:0;width:340px;height:341px}
  .brand{position:absolute;left:20px;top:44px;width:245px;text-align:center;font-family:"Montserrat",sans-serif}
  .brand-mark{display:block;width:70px;height:70px;margin:0 auto 10px;background:var(--link)}
  .brand-name{font-family:"Poppins",sans-serif;font-weight:700;font-size:22px;color:var(--navy);letter-spacing:.02em}
  .brand-url{display:block;margin-top:14px;font-size:13px;color:var(--link);text-decoration:underline}
  .brand-firm{margin-top:3px;font-weight:600;font-size:13.5px;color:var(--ink);letter-spacing:.02em}
  .brand-role{display:flex;align-items:center;gap:6px;font-size:8.5px;font-weight:600;letter-spacing:.14em;color:var(--ink)}
  .brand-role::before,.brand-role::after{content:"";flex:1;height:1px;background:var(--ink)}
  .headline{position:absolute;left:358px;top:26px;width:702px;text-align:center;font-family:"Poppins",sans-serif;font-weight:800;font-size:78px;line-height:1;color:var(--white);text-shadow:0 2px 6px rgba(0,0,0,.45);white-space:nowrap}
  .tagline{position:absolute;left:357px;top:115px;width:701px;height:40px;background:var(--sky);font-family:"Bebas Neue",sans-serif;font-size:35px;line-height:42px;color:var(--white);letter-spacing:.33em;padding-left:16px;white-space:nowrap}
  .site{position:absolute;left:358px;top:168px;width:702px;text-align:center;font-family:"Poppins",sans-serif;font-weight:600;font-size:44px;line-height:1;color:var(--white);text-shadow:0 2px 5px rgba(0,0,0,.45)}
  .call{position:absolute;left:390px;top:227px;width:480px;height:86px}
  .call svg{position:absolute;inset:0}
  .call-label{position:absolute;left:91px;top:5px;font-family:"Bebas Neue",sans-serif;font-size:33px;line-height:1;color:var(--white)}
  .call-number{position:absolute;left:101px;top:38px;font-family:"Poppins",sans-serif;font-weight:800;font-size:39px;line-height:1;color:var(--ink);letter-spacing:-.01em}
  .honor-badge{position:absolute;left:890px;top:272px;width:110px;height:34px;border:2px solid var(--white);border-radius:5px}
</style>
</head>
<body>
  <section class="billboard">
    <div class="backdrop" role="img" aria-label="Night-blue photograph of an industrial oil field with pump jacks and derricks"></div>

    <svg class="brand-panel" viewBox="0 0 340 341" aria-hidden="true">
      <path d="M0 0 H286 C352 70 346 200 186 341 H0 Z" fill="var(--sky)"/>
      <path d="M0 0 H271 C336 70 330 200 172 341 H0 Z" fill="var(--white)"/>
    </svg>

    <div class="brand">
      <span class="brand-mark"></span>
      <div class="brand-name">HOP</div>
      <span class="brand-url">www.hop-law.com</span>
      <div class="brand-firm">HALVERN OSTRAND PIKE</div>
      <div class="brand-role">ATTORNEYS</div>
    </div>

    <h1 class="headline">SERIOUS INJURIES</h1>
    <p class="tagline">TRUSTED. LOCAL. EXPERIENCED.</p>
    <p class="site">www.hop-law.com</p>

    <div class="call">
      <svg viewBox="0 0 480 86" aria-hidden="true">
        <polygon points="74,4 232,4 246,34 74,34" fill="var(--sky)"/>
        <polygon points="64,35 424,35 467,79 64,79" fill="var(--white)"/>
        <circle cx="43" cy="40" r="40" fill="var(--navy-deep)"/>
        <circle cx="43" cy="40" r="36" fill="var(--sky)"/>
        <circle cx="43" cy="40" r="29" fill="none" stroke="var(--white)" stroke-width="2.5"/>
        <path d="M30 27 l6 -3 l5 9 l-4 3 c2 5 5 8 10 10 l3 -4 l9 5 l-3 6 c-13 1 -27 -13 -26 -26 z" fill="var(--white)"/>
        <path d="M46 24 l2 5 M52 26 l-2 5 M57 31 l-5 2" stroke="var(--white)" stroke-width="2" stroke-linecap="round"/>
      </svg>
      <span class="call-label">CALL US NOW</span>
      <span class="call-number">+1 555-014-2280</span>
    </div>

    <div class="honor-badge" role="img" aria-label="Brightvale Honors rating badge"></div>
  </section>
</body>
</html>
```